Flyer-Design für Datenschutzorganisation
Zielgruppe
Unsere Zielgruppe sind mittelständische Unternehmen ohne Ärzte und Apotheken, Mitarbeiterzahl 1-100 Personen, wir unterstützen Unternehmer und Unternehmen bei der Umsetzung der EU-Datenschutzgrundverordnung im Betrieb, wir sind ein VORTA-zertifiziertes Beratungsunternehmen
Aufgabenstellung
'Unsere vornehmliche Aufgabe liegt im Aufbau und der Umsetzung einer praxisnahen und gesetzeskonformen Datenschutzorganisation in Ihrem Unternehmen.'
'Nur wer alle Regeln kennt, kann sie auch einhalten'
'Egal, ob aus Ressourcengründen oder um den Blick eines externen Experten zu erhalten – unsere Beratung macht Sinn. Im Mittelpunkt steht dabei immer Ihr Unternehmen, Ihre Mitarbeiter und Ihre Projekte.'
'Wir sorgen für eine datenschutzkonforme Ausgestaltung der Prozesse in Ihrem Unternehmen im Umgang mit personenbezogenen Daten, ausgerichtet an der Zielsetzung Ihres Geschäftsmodells. Sie erhalten somit ein Rundum-sorglos-Paket im Datenschutz.'

```html
<!DOCTYPE html>
<html lang="de">
<head>
<meta charset="utf-8">
<title>Flyer Datenschutzorganisation</title>
<link rel="stylesheet" href="https://fonts.googleapis.com/css2?family=Oswald:wght@500&family=Quicksand:wght@500&display=swap">
<style>
  :root {
    --stage: #d9d9d9;
    --paper: #ffffff;
    --navy: #0b1140;
    --deep-blue: #0a2463;
    --mid-blue: #0d4f9a;
    --cyan: #12a7cc;
    --text: #2a2a2a;
    --headline-box: rgba(190, 215, 235, 0.55);
  }
  * { margin: 0; padding: 0; box-sizing: border-box; }
  html, body { width: 1200px; height: 800px; overflow: hidden; background: var(--stage); }
  .canvas { position: relative; width: 1200px; height: 800px; }

  .panel {
    position: absolute;
    width: 520px;
    height: 250px;
    background: var(--paper);
    overflow: hidden;
    box-shadow: 0 4px 14px rgba(0,0,0,0.15);
  }

  /* Cover */
  .cover {
    left: 340px; top: 60px;
    background: linear-gradient(110deg, var(--deep-blue) 0%, var(--mid-blue) 55%, var(--cyan) 100%);
  }
  .cover-visual {
    position: absolute; left: 40px; top: 20px; width: 300px; height: 220px;
    background: radial-gradient(ellipse at 45% 45%, rgba(120,220,235,0.55) 0%, rgba(30,120,180,0.25) 45%, rgba(10,40,100,0) 75%);
  }
  .cover-headline {
    position: absolute; right: 18px; top: 32px;
    background: var(--headline-box);
    border-radius: 10px 0 0 0;
    padding: 8px 14px 8px 14px;
    font-family: "Oswald", sans-serif;
    font-weight: 500;
    color: #ffffff;
    text-transform: uppercase;
    line-height: 1.25;
  }
  .cover-headline .line-1 { display: block; font-size: 16px; letter-spacing: 0.2px; }
  .cover-headline .line-2 { display: block; font-size: 19px; letter-spacing: 0.2px; }

  /* Inside spread */
  .spread-left { left: 80px; top: 400px; }
  .spread-right { left: 600px; top: 400px; }

  .inside-visual-top {
    position: absolute; left: 0; top: 0; width: 470px; height: 118px;
    border-radius: 0 0 26px 0;
    background: linear-gradient(100deg, #123566 0%, #1b4f86 45%, #0d2344 100%);
  }
  .body-copy {
    font-family: "Quicksand", sans-serif;
    font-weight: 500;
    font-size: 11.5px;
    line-height: 1.45;
    color: var(--text);
  }
  .spread-left .body-copy {
    position: absolute; left: 38px; top: 140px; width: 450px; font-style: italic;
  }
  .bar { position: absolute; height: 5px; background: var(--navy); }
  .spread-left .bar { left: 0; bottom: 14px; width: 470px; }
  .spread-right .bar { right: 0; top: 0; width: 470px; }

  .spread-right .body-copy { position: absolute; left: 60px; top: 20px; width: 440px; }
  .spread-right .body-copy p + p { margin-top: 8px; }
  .inside-visual-bottom {
    position: absolute; right: 0; bottom: 0; width: 470px; height: 112px;
    border-radius: 22px 0 0 0;
    background: linear-gradient(95deg, #6a6c73 0%, #a9a294 45%, #d8d4cc 75%, #8a8078 100%);
  }
</style>
</head>
<body>
<main class="canvas">

  <section class="panel cover">
    <div class="cover-visual" role="img" aria-label="Leuchtendes Vorhängeschloss aus Netzlinien über einem Laptop"></div>
    <h1 class="cover-headline">
      <span class="line-1">Nur wer alle Regeln kennt,</span>
      <span class="line-2">kann sie auch einhalten</span>
    </h1>
  </section>

  <section class="panel spread-left">
    <div class="inside-visual-top" role="img" aria-label="Geschäftsmann berührt ein digitales Schloss-Symbol in einem Datennetz"></div>
    <p class="body-copy">Unsere vornehmliche Aufgabe liegt im Aufbau und der Umsetzung einer praxisnahen und gesetzeskonformen Datenschutzorganisation in Ihrem Unternehmen.</p>
    <div class="bar"></div>
  </section>

  <section class="panel spread-right">
    <div class="bar"></div>
    <div class="body-copy">
      <p>Egal, ob aus Ressourcengründen oder um den Blick eines externen Experten zu erhalten – unsere Beratung macht Sinn.</p>
      <p>Im Mittelpunkt steht dabei immer Ihr Unternehmen, Ihre Mitarbeiter und Ihre Projekte.</p>
    </div>
    <div class="inside-visual-bottom" role="img" aria-label="Besprechung am Schreibtisch mit Laptop, Notizen und Stift"></div>
  </section>

</main>
</body>
</html>
```